Sleek Design For Personal Brand Wordpress Website !!

*WORDPRESS WEBSITE*

Need a sleek and easy to navigate Wordpress website.

It will act as the hub for my personal brand.

Which means it will showcase all my social media outlets, host my most recent content like youtube videos and podcasts...

It will also be the go to place to find all my digital products and services that I offer.

i want it to be super sleek and simple but also give a personal touch of my who I really am. You can get a good idea of who I am my checking out my Instagram (@karel.dumonte)

Use these websites for ideas: www.brevanhollis.example and www.dorianfelkowitz.example

Target Market(s)

Young Entrepreneurs

Industry/Entity Type

Education

Logo Text

Karel Dumonte

Number of Pages Required

4 page

Font styles to use
Sans Serif

Colors
ffffff
0392cd
ec1f27

Requirements
Must have
• Social Media buttons on the home page...
• Video (also a slider) right at the top of the home page...
• Email Optin...
• Multiple pages...

```html
<!DOCTYPE html>
<html lang="en">
<head>
<meta charset="utf-8">
<title>Dumonte Media</title>
<link href="https://fonts.googleapis.com/css2?family=Raleway:wght@400;600;700;800&family=Open+Sans:wght@400;600;700&display=swap" rel="stylesheet">
<style>
:root{
  --blue:#0392cd;
  --red:#ec1f27;
  --white:#ffffff;
  --ink:#222a30;
  --muted:#7a8288;
  --line:#d9dde0;
  --dark:#1d2428;
  --yellow:#f2c318;
}
*{box-sizing:border-box;margin:0;padding:0}
html,body{width:1200px;height:3688px;overflow:hidden;background:var(--white)}
body{font-family:"Open Sans",sans-serif;color:var(--ink);position:relative}
h1,h2,h3,h4,.logo,.nav a{font-family:"Raleway",sans-serif}
.section{position:absolute;left:0;width:1200px}
.btn{display:inline-block;background:var(--red);color:var(--white);font-family:"Raleway",sans-serif;font-weight:700;font-size:15px;padding:12px 24px;border-radius:3px;text-decoration:none;white-space:nowrap}
.photo{position:absolute}
.play{position:absolute;width:76px;height:76px;border-radius:50%;background:rgba(255,255,255,.9);left:50%;top:50%;transform:translate(-50%,-50%)}
.play::after{content:"";position:absolute;left:30px;top:22px;border-left:24px solid var(--blue);border-top:16px solid transparent;border-bottom:16px solid transparent}

/* header */
.header{top:0;height:112px;background:var(--white);border-bottom:1px solid var(--line)}
.toplinks{position:absolute;right:100px;top:8px;font-size:13px;color:var(--muted)}
.logo{position:absolute;left:100px;top:50px;font-size:36px;font-weight:800;color:var(--blue)}
.nav{position:absolute;left:496px;top:66px;display:flex;gap:22px;white-space:nowrap}
.nav a{font-size:14px;font-weight:700;color:var(--ink);text-decoration:none}
.nav a.active{color:var(--red)}
.header .btn{position:absolute;left:924px;top:54px;padding:11px 24px;font-size:14px}

/* hero */
.hero{top:112px;height:448px;background:linear-gradient(90deg,#4ba9d6,#8bc6e4 45%,#5ab1dc);}
.hero .play{width:84px;height:84px}

/* stats */
.stats{top:560px;height:160px;display:flex;justify-content:center;gap:48px;padding-top:54px}
.stat{display:flex;align-items:center;gap:10px}
.stat .dot{width:34px;height:34px;border-radius:50%}
.stat b{display:block;font-size:15px;color:var(--ink)}
.stat span{font-size:11px;color:var(--muted);letter-spacing:1px}

/* about */
.about{top:720px;height:400px}
.about h2{position:absolute;left:100px;top:10px;font-size:30px;font-weight:800;letter-spacing:1px}
.about p{position:absolute;left:100px;width:490px;font-size:14px;line-height:24px;color:var(--muted)}
.about .btn{position:absolute;left:100px;top:250px}
.about .video{left:624px;top:10px;width:476px;height:290px;background:linear-gradient(160deg,#3b4650,#6c7a86 60%,#a7b4be)}
.about .more{position:absolute;left:824px;top:312px;font-size:14px;font-weight:700;color:var(--blue);text-decoration:underline}

/* conference */
.conference{top:1132px;height:248px;background:linear-gradient(90deg,#23404e,#3d6476 50%,#23404e);text-align:center;color:var(--white)}
.conference h2{margin-top:52px;font-size:28px;font-weight:800;letter-spacing:1px}
.conference p{width:820px;margin:14px auto 22px;font-size:14px;line-height:22px;color:#e6eef2}

/* services */
.services{top:1380px;height:600px;text-align:center}
.section-title{font-size:28px;font-weight:800;letter-spacing:1px}
.services .section-title{margin-top:140px}
.service-grid{position:absolute;left:100px;top:208px;display:flex;gap:20px}
.service{width:240px}
.service .thumb{height:232px}
.service h4{font-size:15px;font-weight:700;margin-top:10px}
.service p{font-size:12px;line-height:18px;color:var(--muted);margin-top:4px}
.service a{display:block;color:var(--red);font-weight:700;font-size:14px;margin-top:6px;text-decoration:none}

/* podcast */
.podcast{top:1980px;height:480px;background:var(--blue);text-align:center;color:var(--white)}
.podcast .section-title{margin-top:84px}
.episodes{position:absolute;left:100px;top:140px;display:flex;gap:22px}
.episode{position:relative;width:318px;height:220px}
.episode .badge{position:absolute;left:50%;top:50%;width:60px;height:60px;border-radius:50%;background:var(--blue);transform:translate(-50%,-50%)}
.episode .label{position:absolute;left:0;right:0;top:28px;font-family:"Raleway",sans-serif;font-weight:800;font-size:20px}

/* contact */
.contact{top:2460px;height:520px}
.contact h2{position:absolute;left:100px;width:560px;top:46px;text-align:center;font-size:28px;font-weight:800;letter-spacing:1px}
.field{position:absolute;height:40px;border:1px solid #b9c0c5;font-size:13px;color:var(--muted);padding:10px 12px;background:var(--white)}
.contact .btn{position:absolute;left:315px;top:396px}
.contact .portrait{left:748px;top:52px;width:352px;height:388px;background:linear-gradient(180deg,#5fb1e2,#c9e4f2 45%,#e8e3d8)}

/* training */
.training{top:2980px;height:440px;background:linear-gradient(180deg,#6d7378,#8a9095);text-align:center;color:var(--white)}
.training .section-title{margin-top:82px;color:var(--ink)}
.lessons{position:absolute;left:100px;top:144px;display:flex;gap:34px}
.lesson{position:relative;width:320px;height:222px;background:linear-gradient(160deg,#3d4a54,#7d8992)}
.lesson h4{position:absolute;left:20px;right:20px;top:80px;font-size:19px;font-weight:800;line-height:24px}

/* footer */
.footer{top:3420px;height:268px;background:linear-gradient(90deg,#12181b,#2b3439 50%,#12181b);color:var(--white)}
.footer .logo{top:110px;color:var(--white)}
.subscribe{position:absolute;left:482px;top:40px}
.subscribe h4{font-size:18px;font-weight:700}
.subscribe .input{margin-top:16px;width:260px;height:38px;background:var(--white);color:var(--muted);font-size:12px;padding:11px 12px;position:relative}
.subscribe .input::after{content:"";position:absolute;right:0;top:0;width:38px;height:38px;background:var(--blue)}
.follow{position:absolute;left:930px;top:40px}
.follow h4{font-size:18px;font-weight:700}
.follow .icons{margin-top:18px;display:flex;gap:14px}
.follow .icons i{width:22px;height:22px;border-radius:50%;background:var(--white);display:block}
.copyright{position:absolute;left:0;right:0;top:226px;text-align:center;font-size:12px;color:#aab3b8;border-top:1px solid #3c464b;padding-top:14px}
</style>
</head>
<body>

<header class="section header">
  <div class="toplinks">Login | Help | Programs | Mail | Cart</div>
  <div class="logo">Dumonte Media</div>
  <nav class="nav"><a class="active">Home</a><a>Blog</a><a>Podcast</a><a>Events</a><a>Hire Me To Speak</a></nav>
  <a class="btn">Join Here for Free</a>
</header>

<section class="section hero" role="img" aria-label="Video slide: Karel Dumonte standing in a bright office, blue tinted">
  <div class="play"></div>
</section>

<section class="section stats">
  <div class="stat"><i class="dot" style="background:var(--red)"></i><div><b>1,984,328</b><span>FRIENDS</span></div></div>
  <div class="stat"><i class="dot" style="background:var(--blue)"></i><div><b>8,293,277</b><span>LIKES</span></div></div>
  <div class="stat"><i class="dot" style="background:#27a9e0"></i><div><b>5,284,822</b><span>FOLLOWERS</span></div></div>
  <div class="stat"><i class="dot" style="background:var(--red)"></i><div><b>8,826,672</b><span>SUBSCRIBERS</span></div></div>
  <div class="stat"><i class="dot" style="background:var(--blue)"></i><div><b>7,092,866</b><span>CONNECTIONS</span></div></div>
  <div class="stat"><i class="dot" style="background:var(--yellow)"></i><div><b>15,418</b><span>FRIENDS</span></div></div>
</section>

<section class="section about">
  <h2>I BUILD BUSINESS</h2>
  <p style="top:62px">Lorem ipsum dolor sit amet, consectetur adipiscing elit, sed do eiusmod tempor incididunt ut labore et dolore magna aliqua. Ut enim ad minim veniam, quis nostrud exercitation.</p>
  <p style="top:154px">Lorem ipsum dolor sit amet, consectetur adipiscing elit, sed do eiusmod tempor incididunt ut labore et dolore magna aliqua ut enim.</p>
  <a class="btn">READ MORE</a>
  <div class="photo video" role="img" aria-label="Video thumbnail: speaker on stage in front of a city skyline"><div class="play"></div></div>
  <span class="more">Watch More</span>
</section>

<section class="section conference" role="img" aria-label="Conference hall with audience and bookshelves, dark blue overlay">
  <h2>WATCH THE DUMONTE'S CONFERENCE ALIVE</h2>
  <p>Lorem ipsum dolor sit amet, consectetur adipiscing elit, sed do eiusmod tempor incididunt ut labore et dolore magna aliqua. Ut enim ad minim veniam, quis nostrud exercitation ullamco laboris nisi ut aliquip ex ea commodo.</p>
  <a class="btn">READ MORE</a>
</section>

<section class="section services">
  <h2 class="section-title">SERVICES</h2>
  <div class="service-grid">
    <div class="service"><div class="thumb" role="img" aria-label="Two people on a rocky coast" style="background:linear-gradient(180deg,#8cb7d8,#5c6b4e)"></div><h4>Conference</h4><p>Lorem ipsum dolor sit amet, consectetur adipiscing elit sed do.</p><a>Read More</a></div>
    <div class="service"><div class="thumb" role="img" aria-label="Private jet on a runway" style="background:linear-gradient(180deg,#cfe3f0,#8a96a0)"></div><h4>Seo For Small Business</h4><p>Lorem ipsum dolor sit amet, consectetur adipiscing elit sed do.</p><a>Read More</a></div>
    <div class="service"><div class="thumb" role="img" aria-label="Crowd at a night event" style="background:linear-gradient(180deg,#2a2230,#7b4a52)"></div><h4>Deal With Stubborn People</h4><p>Lorem ipsum dolor sit amet, consectetur adipiscing elit sed do.</p><a>Read More</a></div>
    <div class="service"><div class="thumb" role="img" aria-label="Man standing on a city street" style="background:linear-gradient(180deg,#a9c6de,#8a7a66)"></div><h4>Coaching</h4><p>Lorem ipsum dolor sit amet, consectetur adipiscing elit sed do.</p><a>Read More</a></div>
  </div>
</section>

<section class="section podcast">
  <h2 class="section-title">PODCAST</h2>
  <div class="episodes">
    <div class="episode" role="img" aria-label="Podcast episode: two men seated in a studio" style="background:linear-gradient(160deg,#3c4a55,#8c7a6a)"><i class="badge"></i></div>
    <div class="episode" role="img" aria-label="Podcast episode: host on a red branded set" style="background:linear-gradient(160deg,#b8262c,#5a2a2e)"><span class="label">Dumonte - On Air</span><i class="badge"></i></div>
    <div class="episode" role="img" aria-label="Podcast episode: group of friends outdoors" style="background:linear-gradient(160deg,#4a5560,#9aa4aa)"><i class="badge"></i></div>
  </div>
</section>

<section class="section contact">
  <h2>GET IN TOUCH WITH US</h2>
  <div class="field" style="left:100px;top:122px;width:262px">Name</div>
  <div class="field" style="left:398px;top:122px;width:262px">Phone No</div>
  <div class="field" style="left:100px;top:186px;width:560px">Email Address</div>
  <div class="field" style="left:100px;top:250px;width:560px;height:120px">Message</div>
  <a class="btn">Register Now</a>
  <div class="photo portrait" role="img" aria-label="Karel Dumonte in a white shirt by the sea"></div>
</section>

<section class="section training" role="img" aria-label="Greyscale backdrop of people at a workshop">
  <h2 class="section-title">WHAT YOU WILL LEARN ON THIS FREE TRAINING</h2>
  <div class="lessons">
    <div class="lesson"><h4>HOW YOU CREATE A PROPERTY STORY THAT CONVERTS</h4></div>
    <div class="lesson" style="background:linear-gradient(160deg,#5a7f98,#c2a88a)"><h4 style="font-size:13px;font-weight:600;line-height:18px;top:20px">Learn how to set up a funnel that turns attention into sales and keeps buyers coming back.</h4></div>
    <div class="lesson"><h4>HOW YOU CAN DRIVE LASER TARGETED TRAFFIC</h4></div>
  </div>
</section>

<footer class="section footer" role="img" aria-label="Dark backdrop of Karel Dumonte with friends">
  <div class="logo">Dumonte Media</div>
  <div class="subscribe"><h4>Subscribe Newsletter</h4><div class="input">Enter Your Email</div></div>
  <div class="follow"><h4>Follow Us On</h4><div class="icons"><i></i><i></i><i></i><i></i></div></div>
  <div class="copyright">© 2017. All Rights Reserved.</div>
</footer>

</body>
</html>
```